Lumora aesthetics offers a range of facial aesthetics treatments by a fully qualified dentist, to a high end crowd. Treatments include antiwrinkle treatment, the use of dermal fillers to provide facial volumisation and rejuvenation and also lip volumisation.
I want a luxurious and bold look. Black background with a bold striking gold logo in the centre possibly incorporating the outline of a face in a subtle yet effective way. I want it to include the work I offer so people will be aware of what they are looking into but not look like there's too much on the card, So it's a clean look.
At the bottom I would like it to say by Dr. Meera Sandhu. Alongside my email address and mobile number.

```html
<!DOCTYPE html>
<html lang="en">
<head>
<meta charset="utf-8">
<title>Lumora Aesthetics – Business Card</title>
<link rel="stylesheet" href="https://fonts.googleapis.com/css2?family=Cinzel:wght@500&family=Open+Sans:wght@400&display=swap">
<style>
  :root {
    --stage: #d8d3cb;
    --card: #121212;
    --gold: #d9b75a;
    --gold-soft: #cfae5e;
  }
  * { margin: 0; padding: 0; box-sizing: border-box; }
  html, body {
    width: 1200px;
    height: 1000px;
    overflow: hidden;
    background: var(--stage);
  }
  .stage {
    width: 1200px;
    height: 1000px;
    display: flex;
    align-items: center;
    justify-content: center;
  }
  .card {
    width: 990px;
    height: 592px;
    background: var(--card);
    border-radius: 40px;
    display: flex;
    flex-direction: column;
    align-items: center;
    color: var(--gold-soft);
    font-family: "Open Sans", Arial, sans-serif;
  }
  .brand-mark {
    width: 128px;
    height: 128px;
    margin-top: 46px;
    border-radius: 50%;
    background: var(--gold);
  }
  .brand-name {
    margin-top: 36px;
    font-family: "Cinzel", Georgia, serif;
    font-weight: 500;
    font-size: 52px;
    letter-spacing: 1px;
    color: var(--gold);
    line-height: 1;
  }
  .services {
    margin-top: 40px;
    font-size: 24px;
    line-height: 34px;
    text-align: center;
  }
  .practitioner {
    margin-top: 38px;
    font-family: "Cinzel", Georgia, serif;
    font-weight: 500;
    font-size: 29px;
    color: var(--gold);
  }
  .contact {
    margin-top: 16px;
    display: flex;
    gap: 36px;
    font-size: 24px;
  }
  .contact-item {
    display: flex;
    align-items: center;
    gap: 10px;
  }
  .contact-item svg { fill: none; stroke: var(--gold-soft); stroke-width: 1.8; }
  .contact-item .icon-mail { fill: var(--gold-soft); stroke: none; }
</style>
</head>
<body>
  <main class="stage">
    <article class="card">
      <div class="brand-mark" aria-hidden="true"></div>
      <h1 class="brand-name">Lumora Aesthetics</h1>
      <p class="services">
        Frown Line - Crows feet • Bunny lines • Neck lines • Eyebrow lift<br>
        Marionette lines • Hyperhidrosis • Glabellar lines • Top lip lines
      </p>
      <h2 class="practitioner">Dr. Meera Sandhu</h2>
      <div class="contact">
        <span class="contact-item">
          <svg width="14" height="24" viewBox="0 0 14 24" aria-hidden="true">
            <rect x="1.5" y="1.5" width="11" height="21" rx="2"/>
            <line x1="5" y1="19" x2="9" y2="19"/>
          </svg>
          + 000 000 0000
        </span>
        <span class="contact-item">
          <svg class="icon-mail" width="22" height="16" viewBox="0 0 22 16" aria-hidden="true">
            <path d="M0 0h22v16H0z M1.5 1.5 11 9l9.5-7.5v13h-19z" fill-rule="evenodd"/>
          </svg>
          info@lumoraaesthetics.com
        </span>
      </div>
    </article>
  </main>
</body>
</html>
```